Whey Protein Packet Label Design

Company background:

Company name: Tidewell Form

Website: tidewellform.com

Summary: We offer single serving supplements on the go that are all natural. We are all about healthy living and portable packaging that makes it easy to drink anywhere. Our Whey Protein Packet saves time and is convenient for our customers to make a protein shake anywhere, there is no prep time, cook time, or clean up time. These protein packets can be added into any shaker and it is easily mixed, no more large bulk tubs of protein needed anymore because we offer single servings that are manageable to carry around.

Style: Our company name is Tidewell Form, so in our logo we are saying that anyone can reach the mountain peak by taking healthy foods. That somehow needs to be shown through a pattern or something.

Products: Whey Protein Packets, Energy Sticks, Recovery Sticks

Product Label Instruction:

I need a product label for the Whey Protein Packet for 5 flavors.
-There should be one generic design, and the flavors just change according to color scheme and pictures

1. Strawberry Banana Smoothie (100% Organic Fruit Powder)
color scheme: Red, white, brown
2. Peanut Butter Smoothie (100% Organic Nut Powder)
color scheme: light brown, brown, white
3. Chocolate Smoothie(100% Organic Cacao Powder)
color scheme: dark brown, brown, white
4. Vanilla Shake (100% Pure Vanilla Powder)
color scheme: light cream, brown, white
5. Banana Peanut Butter Shake (100% Organic Fruit & Nut Powder)
color scheme: yellow, brown, white

Each flavor label design should have this text/information on the front:

1. Logo (attached) - does not need to be main part of design( just placed somewhere is fine)
2. Natural Whey Protein Packet (product title)
3. Flavor Name
4. Flavor Picture
5. 30G (amount of protein in each packet)
6. 4 professional stamps that easily state (attached an image for example)
1. Non GMO
2. Gluten Free
3. Lactose Free
4. No Artificial Flavoring
7. Net Weight 36G

Colors: I would like to use flavor color, brown, and white mainly for the packaging but I am open to different colors for diff flavors and colorful pictures.

Ideas: Please give me multiple designs to look at for the first draft.

Other company examples: I have attached some pictures of other packaging designs that I like that you can keep in mind.

Target Market(s)

Upscale, organic lifestyle, vegans, on the go people, police force, outdoor people, health junkies, gym goers, men and women

I hope you can make something that will appeal to most or all of these categories.

Industry/Entity Type

It Company

Requirements
Must have
• label dimensions: 3 x 3.75
• font: Unique, not something basic that looks like it came off of word document. It needs to look professional and unique that the upscale market would like.
Nice to have
• I have attached some examples of other companies that I like the look of. That is the type of style I am going for.
Should not have
• It should not be a basic design that I can make myself. I am looking for a professional who can make the product look like an organic style and shows that we offer HIGH QUALITY, high end supplements.

```html
<!DOCTYPE html>
<html lang="en">
<head>
<meta charset="UTF-8">
<title>Tidewell Form – Strawberry Banana Smoothie Label</title>
<link rel="stylesheet" href="https://fonts.googleapis.com/css2?family=Josefin+Sans:wght@300;400&family=Kristi&display=swap">
<style>
  :root {
    --backdrop: #f1e4d8;
    --kraft: #c7b393;
    --kraft-light: #d2bfa2;
    --kraft-dark: #b9a47f;
    --label-white: #ffffff;
    --berry-red: #e10d12;
    --deep-red: #b8090d;
    --cocoa-text: #6a1a12;
    --banana: #f3d23a;
    --strawberry: #d42a22;
  }
  * { margin: 0; padding: 0; box-sizing: border-box; }
  html, body { width: 1200px; height: 848px; overflow: hidden; }
  body {
    background: var(--backdrop);
    position: relative;
    font-family: "Josefin Sans", sans-serif;
  }
  .label {
    position: absolute;
    left: 383px; top: 152px;
    width: 434px; height: 544px;
    background: radial-gradient(ellipse at 40% 45%, var(--kraft-light), var(--kraft) 60%, var(--kraft-dark));
    box-shadow: 0 2px 6px rgba(90, 60, 40, 0.18);
    overflow: hidden;
  }
  .brand-band {
    position: absolute; left: 0; top: 0;
    width: 100%; height: 66px;
    background: var(--label-white);
  }
  .brand-name {
    position: absolute; left: 86px; right: 0; top: 20px;
    text-align: center;
    font-weight: 300;
    font-size: 24px;
    letter-spacing: 5px;
    color: var(--berry-red);
  }
  .product-title {
    position: absolute; left: 100px; right: 10px; top: 68px;
    text-align: center;
    font-family: "Kristi", cursive;
    font-size: 31px;
    color: var(--label-white);
  }
  .accent-band {
    position: absolute; left: 0; top: 112px;
    width: 100%; height: 11px;
    background: var(--berry-red);
  }
  .ribbon {
    position: absolute; left: 26px; top: 0;
    width: 60px; height: 304px;
  }
  .ribbon-text {
    position: absolute; left: 56px; top: 255px;
    transform-origin: 0 0;
    transform: rotate(-90deg);
    width: 250px;
    font-family: "Kristi", cursive;
    font-size: 30px;
    line-height: 1;
    color: var(--label-white);
    white-space: nowrap;
  }
  .flavor-name {
    position: absolute; left: 109px; top: 130px;
    font-weight: 400;
    font-size: 45px;
    line-height: 48px;
    color: var(--label-white);
    text-shadow: 2px 2px 0 var(--berry-red);
  }
  .flavor-photo {
    position: absolute; left: 103px; top: 280px;
    width: 282px; height: 204px;
    border-radius: 46% 54% 48% 52% / 55% 50% 50% 45%;
    background:
      radial-gradient(circle at 35% 70%, var(--strawberry) 0 22%, transparent 23%),
      radial-gradient(ellipse at 60% 45%, var(--banana) 0 45%, transparent 60%),
      linear-gradient(135deg, #e9c63a, #d9a92a);
    opacity: 0.95;
  }
  .stamp {
    position: absolute; left: 20px;
    width: 72px; height: 72px;
  }
  .stamp-allergen { top: 318px; }
  .stamp-natural { top: 405px; }
  .protein-amount {
    position: absolute; left: 6px; width: 100px; top: 486px;
    text-align: center;
    font-size: 16px;
    line-height: 16px;
    color: var(--cocoa-text);
  }
  .net-weight {
    position: absolute; left: 270px; top: 510px;
    font-size: 17px;
    color: var(--cocoa-text);
    white-space: nowrap;
  }
</style>
</head>
<body>
  <main class="label">
    <div class="brand-band">
      <div class="brand-name">Tidewell Form</div>
    </div>

    <div class="product-title">Natural Whey Protein Packet</div>
    <div class="accent-band"></div>

    <svg class="ribbon" viewBox="0 0 60 304" aria-hidden="true">
      <polygon points="0,0 60,0 60,304 30,286 0,304" fill="var(--berry-red)"/>
    </svg>
    <div class="ribbon-text">100% Organic Fruit Powder</div>

    <h1 class="flavor-name">Strawberry<br>Banana<br>Smoothie</h1>

    <div class="flavor-photo" role="img" aria-label="Photo of ripe bananas with whole and halved strawberries"></div>

    <svg class="stamp stamp-allergen" viewBox="0 0 72 72" role="img" aria-label="Gluten free and lactose free stamp">
      <circle cx="36" cy="36" r="35" fill="var(--label-white)" opacity="0.35"/>
      <circle cx="36" cy="36" r="33" fill="none" stroke="var(--label-white)" stroke-width="2"/>
      <circle cx="36" cy="36" r="23" fill="none" stroke="var(--label-white)" stroke-width="1.5"/>
    </svg>
    <svg class="stamp stamp-natural" viewBox="0 0 72 72" role="img" aria-label="Non GMO and no artificial flavoring stamp">
      <circle cx="36" cy="36" r="35" fill="var(--label-white)" opacity="0.35"/>
      <circle cx="36" cy="36" r="33" fill="none" stroke="var(--label-white)" stroke-width="2"/>
      <circle cx="36" cy="36" r="23" fill="none" stroke="var(--label-white)" stroke-width="1.5"/>
    </svg>

    <p class="protein-amount">30g<br>of protein</p>
    <p class="net-weight">Net Weight 36g</p>
  </main>
</body>
</html>
```